基本レイアウトについては
https://zumelo.com/diagrams/XR8k21pTbvNDWfeL
もしくは、添付データのワイヤーをご参照ください。
レイアウトについては必ずしも上記に準じている必要はありません。
ご自由にご提案いただいても結構です。

全体の雰囲気としては
http://www.tomirei-wedding.net/
http://www.hokumorisanjingu.or.jp/
のような、桜色をつかいながら
あまり古臭くなり過ぎないようにアピールできればと思います。

また、製品は
http://www.seiryu-kojin.co.jp/goods/luvasystem
http://www.gw-tmr.co.jp/
のものを使用しています。

美容室へ来られる方は、近隣の方が多く、
和髪以外での競争力はあまりないため、WEB上では
美容師への和髪の講習などの訴求時に、
信頼性を高めるような用途が多くなりそうです。

そのため、上記参考サイトのような
ちょっとしたスタイリッシュさを目指しています。
http://qrvmd.ozu.ne.jp/0597214483/index.html
ホワイト、桜色をベースに、落ち着いた印象に出来ればと存じます。
素材については、
下記URLよりダウンロードしたものをご利用いただければ幸甚です。
http://plumvault.jp/download/a4f19e02bd7753c6e1088f2d94ab37c51e0d2a96

こちらだけですと、制作が難しいと思いますので
http://mobre.jp/
などから、5000円程度までならこちらにて購入可能です。カンプデータにて作成頂き、
納品時に当方にて購入したデータに差し替えていただければと存じます。

【参考サイト】
↑色合い、印象が気に入っています

http://www.gw-tmr.co.jp/
↑使用している製品のホームページです

http://basement-parts.com/2012/166.html
http://basement-parts.com/2011/115.html
↑フッター部分の参照です

基本レイアウト
については、必ずしも忠実である必要はありません。

是非ご提案お待ちしております。
何卒よろしくお願いいたします。

クライアント様との協議の結果こちらの案を採用させていただきました。
上品さと柔らかさのバランスがとてもよく、
視認性も高く、要望を全て満たしておりましたので
こちらの案を採用いたしました。

この度は多数ご提案いただきありがとうございました。
当選に至らなかったランサー様におかれましては大変心苦しいのですが、
またの機会にぜひご提案いただければ幸甚です。
引き続き何卒よろしくお願いいたします。

```html
<!DOCTYPE html>
<html lang="ja">
<head>
<meta charset="utf-8">
<title>ミハナ美容室</title>
<link href="https://fonts.googleapis.com/css2?family=Noto+Serif+JP:wght@400;600;700&family=Noto+Sans+JP:wght@400;500;700&display=swap" rel="stylesheet">
<style>
:root{
  --pink:#e6739a;
  --pink-deep:#d85583;
  --pink-soft:#f8dbe5;
  --pink-pale:#fcf0f4;
  --ink:#4a4a4a;
  --ink-soft:#808080;
  --line:#e4e4e4;
  --nav:#f4f4f4;
  --white:#ffffff;
}
*{margin:0;padding:0;box-sizing:border-box}
html,body{width:839px;height:1200px;overflow:hidden;background:var(--white)}
body{font-family:"Noto Sans JP",sans-serif;color:var(--ink);font-size:10px;position:relative}

.site-header{position:absolute;left:0;top:0;width:839px;height:96px}
.site-header .logo{position:absolute;left:62px;top:30px;font-family:"Noto Serif JP",serif;font-size:22px;font-weight:600;color:var(--ink);display:flex;align-items:center;gap:8px;white-space:nowrap}
.site-header .logo .dot{width:10px;height:10px;border-radius:50%;background:var(--pink)}
.header-contact{position:absolute;right:58px;top:12px;width:200px}
.header-contact .tel{display:flex;align-items:center;gap:6px;font-size:20px;line-height:26px;font-weight:700;color:var(--pink-deep);letter-spacing:.3px;white-space:nowrap}
.header-contact .tel .badge{font-size:8px;line-height:1.4;color:var(--white);background:var(--pink);padding:2px 5px;border-radius:2px;font-weight:500;white-space:nowrap}
.header-contact p{font-size:8px;color:var(--ink-soft);line-height:1.6;margin-top:4px;white-space:nowrap}

.global-nav{position:absolute;left:0;top:96px;width:839px;height:30px;background:var(--nav);border-top:1px solid var(--line);border-bottom:1px solid var(--line)}
.global-nav ul{list-style:none;display:flex;margin-left:62px;width:720px;height:100%}
.global-nav li{flex:1;display:flex;align-items:center;justify-content:center;font-size:10px;color:var(--ink);border-right:1px solid var(--line)}
.global-nav li.current{color:var(--pink-deep)}

.hero{position:absolute;left:0;top:127px;width:839px;height:226px;background:linear-gradient(90deg,#fbe6ee 0%,#fdf4f7 40%,#f9dfe8 100%);overflow:hidden}
.hero .petals{position:absolute;left:0;top:0;width:839px;height:226px;background:linear-gradient(180deg,rgba(255,255,255,.5),rgba(255,255,255,0))}
.hero .catch{position:absolute;left:126px;top:92px;font-family:"Noto Serif JP",serif;font-size:20px;font-weight:600;color:var(--ink);white-space:nowrap;line-height:1.2}
.hero .catch em{font-style:normal;font-size:32px;color:var(--pink-deep)}
.hero .sub{position:absolute;left:300px;top:152px;font-size:10px;color:var(--pink-deep);line-height:1.8}
.hero .products{position:absolute;left:120px;top:148px;width:160px;height:72px;border-radius:4px;background:linear-gradient(180deg,#f4f4f6,#d9dade)}
.hero .portrait{position:absolute;left:520px;top:0;width:319px;height:226px;background:linear-gradient(135deg,#f6d9e2 0%,#ead3c6 55%,#c9b1a6 100%)}

.sidebar{position:absolute;left:62px;top:410px;width:282px}
.contact-box{border:1px solid var(--line);padding:12px 14px;height:142px;background:var(--white)}
.contact-box h3{font-size:11px;color:var(--pink-deep);font-weight:500;display:flex;align-items:center;gap:6px}
.contact-box .tel{font-size:21px;font-weight:700;color:var(--pink-deep);margin-top:10px;display:flex;align-items:center;gap:6px;white-space:nowrap}
.contact-box p{font-size:9px;color:var(--ink-soft);line-height:1.7;margin-top:8px}
.side-menu{margin-top:20px;border:1px solid var(--line)}
.side-menu h3{background:var(--pink);color:var(--white);text-align:center;padding:7px 0 6px;font-family:"Noto Serif JP",serif;font-size:10px;font-weight:400;line-height:1.3}
.side-menu h3 span{display:block;font-size:9px;opacity:.9}
.side-menu ul{list-style:none}
.side-menu li{font-size:10px;padding:0 14px;height:31px;display:flex;align-items:center;gap:8px;border-top:1px solid var(--line)}
.side-menu li::before{content:"";width:5px;height:5px;border-top:1.5px solid var(--pink);border-right:1.5px solid var(--pink);transform:rotate(45deg)}
.lesson-banner{margin-top:14px;height:128px;border:1px solid var(--line);position:relative;background:var(--pink-pale);overflow:hidden}
.lesson-banner h4{position:absolute;left:12px;top:12px;font-family:"Noto Serif JP",serif;font-size:15px;color:var(--pink-deep);font-weight:600;white-space:nowrap}
.lesson-banner p{position:absolute;left:12px;top:42px;font-size:8.5px;line-height:1.7;color:var(--ink)}
.lesson-banner .photo{position:absolute;right:0;top:0;width:120px;height:128px;background:linear-gradient(180deg,#ecd5dc,#cfb4ba)}

.main{position:absolute;left:372px;top:410px;width:410px}
.section-title{font-family:"Noto Serif JP",serif;font-size:15px;font-weight:600;color:var(--ink);padding-bottom:8px;border-bottom:1px solid var(--line);display:flex;align-items:center;gap:8px}
.section-title::before{content:"";width:4px;height:16px;background:var(--pink)}
.news{list-style:none;margin-top:8px}
.news li{display:flex;gap:14px;font-size:9px;height:25px;align-items:center;border-bottom:1px dotted var(--line)}
.news time{color:var(--ink-soft);width:78px}
.news a{color:var(--pink-deep);text-decoration:none}
.welcome{margin-top:28px}
.welcome-body{position:relative;height:320px;margin-top:12px}
.welcome-body .lead{position:absolute;left:0;top:0;width:232px;font-size:9px;line-height:1.9}
.welcome-body .shop{position:absolute;right:0;top:2px;width:164px;height:130px;background:linear-gradient(180deg,#d9e6dc,#9fb9a6)}
.welcome-body .staff{position:absolute;left:0;top:150px;width:180px;height:130px;background:linear-gradient(180deg,#e7dfe0,#b8a8a8)}
.welcome-body .staff-text{position:absolute;left:196px;top:150px;width:214px;font-size:9px;line-height:1.9}
.welcome-body .more{position:absolute;left:196px;top:262px;font-size:9px;color:var(--pink-deep);display:flex;align-items:center;gap:5px}

.pagetop{position:absolute;right:58px;top:1052px;font-size:8px;color:var(--ink-soft)}
.site-footer{position:absolute;left:0;top:1068px;width:839px;height:132px;border-top:4px solid var(--pink);background:var(--white)}
.site-footer .inner{position:absolute;left:62px;top:14px;width:720px}
.site-footer .f-logo{font-family:"Noto Serif JP",serif;font-size:15px;font-weight:600;display:flex;align-items:center;gap:6px}
.site-footer .f-logo .dot{width:8px;height:8px;border-radius:50%;background:var(--pink)}
.site-footer .f-info{font-size:8px;color:var(--ink-soft);line-height:1.7;margin-top:6px;width:260px}
.site-footer .f-info b{color:var(--pink-deep);font-size:11px}
.f-links{position:absolute;left:340px;top:4px;display:grid;grid-template-columns:repeat(3,120px);row-gap:8px;list-style:none}
.f-links li{font-size:8.5px;display:flex;align-items:center;gap:5px}
.f-links li::before{content:"";width:4px;height:4px;background:var(--pink)}
.copyright{position:absolute;left:0;bottom:0;width:839px;height:22px;background:var(--pink-soft);font-size:8px;color:var(--ink-soft);display:flex;align-items:center;padding-left:62px}
</style>
</head>
<body>

<header class="site-header">
  <div class="logo"><span class="dot"></span>ミハナ美容室</div>
  <div class="header-contact">
    <div class="tel">
      <svg width="14" height="14" viewBox="0 0 24 24"><path fill="#d85583" d="M6.6 10.8a15 15 0 0 0 6.6 6.6l2.2-2.2a1 1 0 0 1 1-.25 11.4 11.4 0 0 0 3.6.6 1 1 0 0 1 1 1V20a1 1 0 0 1-1 1A17 17 0 0 1 3 4a1 1 0 0 1 1-1h3.5a1 1 0 0 1 1 1c0 1.25.2 2.45.6 3.6a1 1 0 0 1-.25 1z"/></svg>
      059-721-4483<span class="badge">ご予約</span>
    </div>
    <p>営業時間 9:00〜18:00／定休日 毎週火曜日<br>東海県北森市青葉町3-12-5</p>
  </div>
</header>

<nav class="global-nav">
  <ul>
    <li class="current">ホーム</li>
    <li>メニュー・料金</li>
    <li>製品へのこだわり</li>
    <li>よくある質問</li>
    <li>店舗案内</li>
  </ul>
</nav>

<section class="hero">
  <div class="petals"></div>
  <div class="products" role="img" aria-label="ヘアケア製品のボトル写真"></div>
  <h1 class="catch"><em>和髪</em>と<em>着付け</em> が得意な美容室です。</h1>
  <p class="sub">髪質と頭皮にやさしい製品を<br>厳選して使用しています。</p>
  <div class="portrait" role="img" aria-label="和髪に結い上げた女性の横顔写真"></div>
</section>

<aside class="sidebar">
  <div class="contact-box">
    <h3>
      <svg width="12" height="12" viewBox="0 0 24 24"><path fill="#e6739a" d="M20 4H4a2 2 0 0 0-2 2v12a2 2 0 0 0 2 2h16a2 2 0 0 0 2-2V6a2 2 0 0 0-2-2zm0 4-8 5-8-5V6l8 5 8-5z"/></svg>
      お気軽にご連絡ください
    </h3>
    <div class="tel">
      <svg width="18" height="18" viewBox="0 0 24 24"><path fill="#d85583" d="M6.6 10.8a15 15 0 0 0 6.6 6.6l2.2-2.2a1 1 0 0 1 1-.25 11.4 11.4 0 0 0 3.6.6 1 1 0 0 1 1 1V20a1 1 0 0 1-1 1A17 17 0 0 1 3 4a1 1 0 0 1 1-1h3.5a1 1 0 0 1 1 1c0 1.25.2 2.45.6 3.6a1 1 0 0 1-.25 1z"/></svg>
      059-721-4483
    </div>
    <p>受付 9：00〜18：00<br>定休日：毎週火曜日・第3水曜日</p>
  </div>

  <nav class="side-menu">
    <h3>Menu<span>メニュー</span></h3>
    <ul>
      <li>メニュー・料金</li>
      <li>製品へのこだわり</li>
      <li>初めての方へ</li>
      <li>よくある質問</li>
      <li>店舗案内</li>
    </ul>
  </nav>

  <div class="lesson-banner">
    <h4>和髪について学ぼう</h4>
    <p>美容師の方へ<br>和髪の講習を行っています。<br>お気軽にご相談ください。</p>
    <div class="photo" role="img" aria-label="和髪の講習の様子の写真"></div>
  </div>
</aside>

<main class="main">
  <section>
    <h2 class="section-title">新着情報</h2>
    <ul class="news">
      <li><time>2013年05月01日</time><a>新商品の取り扱いを開始しました</a></li>
      <li><time>2013年04月20日</time><a>五月の定休日についてのお知らせ</a></li>
      <li><time>2013年04月10日</time><a>和髪講習会の日程を更新しました</a></li>
      <li><time>2013年04月01日</time><a>春の着付けキャンペーンのご案内</a></li>
      <li><time>2013年03月15日</time><a>ホームページを公開いたしました</a></li>
    </ul>
  </section>

  <section class="welcome">
    <h2 class="section-title">ミハナ美容室へようこそ</h2>
    <div class="welcome-body">
      <p class="lead">ミハナ美容室は、ゆったりと寛げる空間で、お客様一人ひとりの髪質に合わせた施術を心がけています。地域の皆さまに長く愛されるお店を目指し、丁寧なカウンセリングを大切にしています。<br><br>また、和髪や着付けを得意としており、成人式や結婚式などの大切な日のお手伝いもいたします。</p>
      <div class="shop" role="img" aria-label="美容室の店舗外観の写真"></div>
      <div class="staff" role="img" aria-label="着物姿のお客様とスタッフの写真"></div>
      <p class="staff-text">経験豊かなスタッフが、お客様の想いに寄り添い、一日を華やかに彩ります。着付けのご予約もお気軽にお問い合わせください。</p>
      <div class="more">
        <svg width="8" height="8" viewBox="0 0 10 10"><path d="M3 1l4 4-4 4" stroke="#d85583" stroke-width="1.6" fill="none"/></svg>
        ミハナ美容室 店舗のご案内
      </div>
    </div>
  </section>
</main>

<div class="pagetop">ページの先頭へ ▲</div>

<footer class="site-footer">
  <div class="inner">
    <div class="f-logo"><span class="dot"></span>ミハナ美容室</div>
    <p class="f-info">〒512-0034 東海県北森市青葉町3-12-5<br><b>059-721-4483</b><br>営業時間 9:00〜18:00 定休日 毎週火曜日</p>
    <ul class="f-links">
      <li>ホーム</li><li>メニュー・料金</li><li>よくある質問</li>
      <li>製品へのこだわり</li><li>店舗案内</li><li>プライバシーポリシー</li>
      <li>初めての方へ</li><li>お問い合わせ</li><li>サイトマップ</li>
    </ul>
  </div>
  <div class="copyright">Copyright (c) Mihana Beauty Salon all rights reserved.</div>
</footer>

</body>
</html>
```